Dental Medical History Form - Content provided

Design a medical history form for a dental practice. Content is provided so all that is needed is the formatting to make it look great and easy to read.

"Patient Information" to include all information contained in top portion of the "Patient Medical History Form" docx file.

"Medical History" should follow the formatting and content of the "Exact Medical History" file as this is what the entry fields look like in our practice software and so we would like it to match.

1st page - Patient info, allergies, medications, antibiotics, joint replacement, pregnancy.

2nd page - Do you have, or have you had, any of the following? . . . . . . .
Updates

Project Deadline Extended Reason: Picked too short of a deadline to start (2 days) Added Monday, February 13, 2017

Target Market(s)

All ages but must be clear enough for elderly to read. Use as much space as possible to keep font size bigger yet keep to two pages

Industry/Entity Type

Dental

Font styles to use
Sans Serif

Requirements
Must have
• All content provided
• Our logo at the top (file provided)
• Century Gothic Font
• Limit to two pages

```html
<!DOCTYPE html>
<html lang="en">
<head>
<meta charset="utf-8">
<title>Facet Dental – Confidential Medical History</title>
<link href="https://fonts.googleapis.com/css2?family=Questrial&family=Montserrat:ital,wght@0,600;1,600&display=swap" rel="stylesheet">
<style>
:root{
  --ink:#1d1d1f;
  --muted:#5a5a5e;
  --brand:#6b6a6e;
  --band-1:#5d5b60;
  --band-2:#9b9b9d;
  --band-3:#c6beb3;
  --band-4:#dddcd8;
  --stage:#f3f3f3;
  --paper:#ffffff;
  --rule:#2a2a2a;
}
*{box-sizing:border-box;margin:0;padding:0}
html,body{width:1200px;height:927px;overflow:hidden}
body{background:var(--stage);font-family:"Questrial",sans-serif;color:var(--ink)}
.canvas{position:relative;width:1200px;height:927px}
.page{position:absolute;width:476px;height:672px;background:var(--paper);font-size:9px;line-height:1}
.page--patient{left:76px;top:56px}
.page--history{left:627px;top:144px}
.band{position:absolute;left:0;right:0;height:6px;display:flex}
.band--top{top:0}.band--bottom{bottom:0}
.band i{flex:1}
.band i:nth-child(1){background:var(--band-1)}
.band i:nth-child(2){background:var(--band-2)}
.band i:nth-child(3){background:var(--band-3)}
.band i:nth-child(4){background:var(--band-4)}
.a{position:absolute;white-space:nowrap}
.brand{position:absolute;color:var(--brand);font-family:"Questrial",sans-serif;font-weight:400;white-space:nowrap;line-height:1}
.practice-address{position:absolute;right:18px;top:22px;text-align:right;font-size:7.6px;line-height:9.6px;font-style:normal}
.title{position:absolute;left:0;right:0;top:69px;text-align:center;font-family:"Montserrat",sans-serif;font-weight:600;font-size:15px;letter-spacing:.1px}
.bold{font-family:"Montserrat",sans-serif;font-weight:600;font-size:8.4px}
.field{position:absolute;display:flex;align-items:flex-end;height:10px;white-space:nowrap}
.field .line{flex:1;border-bottom:.8px solid var(--rule);margin-left:1px;height:8px}
.hint{position:absolute;font-size:5.2px;font-style:italic;color:var(--muted)}
.box{position:absolute;width:8px;height:8px;border:.8px solid var(--rule);background:#fff}
.rule{position:absolute;height:0;border-bottom:.8px solid var(--rule)}
.tick{display:inline-block;width:13px;height:13px;vertical-align:-3px;margin-left:2px}
.small{font-size:7.8px}
.turnover{position:absolute;right:41px;top:633px;font-family:"Montserrat",sans-serif;font-weight:600;font-style:italic;font-size:8.4px}

/* history page */
.question{position:absolute;left:23px;top:77px;font-size:9.2px}
.col{position:absolute}
.col--left{left:22px;width:240px}
.col--right{left:270px;width:186px}
.group{position:absolute;left:0;right:0}
.group__title{font-family:"Montserrat",sans-serif;font-weight:600;font-size:8px;height:10px}
.row{position:relative;height:10.45px;font-size:8.3px;line-height:10.45px;white-space:nowrap}
.row--tall{height:20.9px;white-space:normal;line-height:10.45px}
.row .y,.row .n{position:absolute;top:0}
.row .box{top:1px}
.col--left .y{left:172px}.col--left .by{left:192px}.col--left .n{left:208px}.col--left .bn{left:224px}
.col--right .y{left:122px}.col--right .by{left:140px}.col--right .n{left:157px}.col--right .bn{left:173px}
.row--tall .y,.row--tall .n{top:-2px}.row--tall .box{top:-1px}
.thanks{position:absolute;left:0;right:0;top:626px;text-align:center;font-style:italic;font-size:6.6px;line-height:9.2px;color:var(--muted)}
</style>
</head>
<body>
<main class="canvas">

  <section class="page page--patient" aria-label="Page one: patient information">
    <div class="band band--top"><i></i><i></i><i></i><i></i></div>

    <div class="brand" style="left:36px;top:32px;font-size:20px">Facet Dental</div>
    <address class="practice-address">
      Facet Dental<br>Suite 4/18 Harbour Rd<br>Seaview NSW 2261<br>(02) 4012 3456
    </address>

    <h1 class="title">CONFIDENTIAL MEDICAL HISTORY</h1>

    <div class="field" style="left:30px;right:236px;top:115px"><span>Name:</span><span class="line"></span></div>
    <span class="hint" style="left:67px;top:131px">Title</span>
    <span class="hint" style="left:110px;top:131px">First</span>
    <span class="hint" style="left:144px;top:131px">Middle</span>
    <span class="hint" style="left:197px;top:131px">Last</span>
    <div class="field" style="left:31px;right:236px;top:140px"><span>Address:</span><span class="line"></span></div>
    <div class="field" style="left:30px;right:294px;top:153px"><span>DOB:</span><span class="line"></span></div>
    <div class="field" style="left:30px;right:236px;top:165px"><span>Email Address:</span><span class="line"></span></div>
    <div class="field" style="left:30px;top:177px"><span>Phone Number(s)</span></div>
    <div class="field" style="left:30px;right:282px;top:191px"><span>Mobile:&nbsp;&nbsp;&nbsp;</span><span class="line"></span></div>
    <div class="field" style="left:30px;right:282px;top:204px"><span>Home:&nbsp;&nbsp;&nbsp;&nbsp;</span><span class="line"></span></div>
    <div class="field" style="left:30px;right:284px;top:217px"><span>Work :&nbsp;&nbsp;&nbsp;</span><span class="line"></span></div>

    <span class="a bold" style="left:30px;top:243px">Emergency Contact Person:</span>
    <div class="field" style="left:30px;right:240px;top:256px"><span>Name:</span><span class="line"></span></div>
    <div class="field" style="left:30px;right:240px;top:269px"><span>Relationship:</span><span class="line"></span></div>
    <div class="field" style="left:30px;right:236px;top:283px"><span>Phone number:</span><span class="line"></span></div>

    <span class="a bold" style="left:248px;top:112px">General Practitioner:</span>
    <div class="field" style="left:248px;right:30px;top:123px"><span>Name:</span><span class="line"></span></div>
    <div class="field" style="left:248px;right:30px;top:135px"><span>Practice Name:</span><span class="line"></span></div>
    <div class="field" style="left:248px;right:56px;top:147px"><span>Phone Number:</span><span class="line"></span></div>
    <span class="a" style="left:248px;top:172px">Do you have a health fund with dental cover?</span>
    <span class="box" style="left:314px;top:183px"></span><span class="a" style="left:324px;top:184px">Yes&nbsp; or</span>
    <span class="box" style="left:356px;top:183px"></span><span class="a" style="left:366px;top:184px">No</span>
    <div class="field" style="left:248px;right:30px;top:195px"><span>If so, what is the name of the fund?</span><span class="line"></span></div>
    <div class="field" style="left:248px;right:170px;top:207px"><span>Fund Number?</span><span class="line"></span></div>
    <span class="a" style="left:248px;top:220px">Priority Number on card:&nbsp; 0&nbsp; 1&nbsp; 2&nbsp; 3&nbsp; 4&nbsp; 5</span>
    <div class="field" style="left:248px;right:42px;top:243px"><span>Occupation:</span><span class="line"></span></div>
    <div class="field" style="left:248px;right:50px;top:255px"><span>Referred by:</span><span class="line"></span></div>

    <span class="a bold" style="left:30px;top:316px;font-size:9px">Please indicate if&nbsp; you are allergic to any of the following<svg class="tick" viewBox="0 0 14 14" aria-hidden="true"><rect x=".5" y="2.5" width="11" height="11" fill="none" stroke="#1d1d1f"/><path d="M3 8l3 3 7-10" fill="none" stroke="#1d1d1f" stroke-width="1.6"/></svg> ?</span>
    <span class="a small" style="left:30px;top:335px">Aspirin</span><span class="box" style="left:106px;top:335px"></span>
    <span class="a small" style="left:130px;top:334px">Codeine</span><span class="box" style="left:172px;top:334px"></span>
    <span class="a small" style="left:195px;top:334px">Penicillin</span><span class="box" style="left:238px;top:334px"></span>
    <span class="a small" style="left:263px;top:334px">Sulfites</span><span class="box" style="left:296px;top:334px"></span>
    <span class="a small" style="left:30px;top:351px">Local Anaesthetic</span><span class="box" style="left:106px;top:352px"></span>
    <span class="a small" style="left:131px;top:351px">Lactose</span><span class="box" style="left:172px;top:351px"></span>
    <span class="a small" style="left:195px;top:351px">Nickel</span><span class="box" style="left:238px;top:351px"></span>
    <span class="a small" style="left:265px;top:351px">Latex</span><span class="box" style="left:296px;top:351px"></span>
    <div class="field" style="left:30px;right:27px;top:371px"><span>Other:</span><span class="line"></span></div>

    <span class="a bold" style="left:30px;top:393px;font-size:9px">Are you currently taking, or have ever taken, any of the following medication<svg class="tick" viewBox="0 0 14 14" aria-hidden="true"><rect x=".5" y="2.5" width="11" height="11" fill="none" stroke="#1d1d1f"/><path d="M3 8l3 3 7-10" fill="none" stroke="#1d1d1f" stroke-width="1.6"/></svg> ?</span>
    <span class="a small" style="left:29px;top:410px">Asthma inhaler</span><span class="box" style="left:116px;top:410px"></span>
    <span class="a small" style="left:146px;top:410px">Anti-epileptics</span><span class="box" style="left:221px;top:410px"></span>
    <span class="a small" style="left:259px;top:410px">Anti-depressants</span><span class="box" style="left:338px;top:410px"></span>
    <span class="a small" style="left:377px;top:410px">Blood Pressure</span><span class="box" style="left:434px;top:411px"></span>
    <span class="a small" style="left:29px;top:426px">Blood Thinners</span><span class="box" style="left:116px;top:425px"></span>
    <span class="a small" style="left:146px;top:426px">Bisphosphonates</span><span class="box" style="left:221px;top:425px"></span>
    <span class="a small" style="left:259px;top:426px">Chemotherapy</span><span class="box" style="left:338px;top:425px"></span>
    <span class="a small" style="left:377px;top:426px">Insulin</span><span class="box" style="left:434px;top:426px"></span>
    <span class="a small" style="left:29px;top:442px">Immunosuppressants</span><span class="box" style="left:116px;top:441px"></span>
    <span class="a small" style="left:146px;top:442px">Steroids</span><span class="box" style="left:221px;top:441px"></span>
    <span class="a small" style="left:259px;top:442px">Oral Contraceptive</span><span class="box" style="left:338px;top:441px"></span>
    <span class="a small" style="left:377px;top:442px">Other</span><span class="box" style="left:434px;top:442px"></span>

    <span class="a bold" style="left:28px;top:463px;font-size:9px">Please specify medication name, dose, and frequency where possible:</span>
    <span class="rule" style="left:30px;width:130px;top:489px"></span><span class="rule" style="left:174px;width:128px;top:489px"></span><span class="rule" style="left:316px;width:130px;top:489px"></span>
    <span class="rule" style="left:30px;width:130px;top:506px"></span><span class="rule" style="left:174px;width:128px;top:506px"></span><span class="rule" style="left:316px;width:130px;top:506px"></span>
    <span class="rule" style="left:30px;width:130px;top:524px"></span><span class="rule" style="left:174px;width:128px;top:524px"></span><span class="rule" style="left:316px;width:130px;top:524px"></span>

    <span class="a bold" style="left:31px;top:538px">Do you require antibiotic cover?</span>
    <span class="a" style="left:204px;top:538px">Yes</span><span class="box" style="left:225px;top:538px"></span>
    <span class="a" style="left:241px;top:538px">No</span><span class="box" style="left:258px;top:538px"></span>
    <span class="a bold" style="left:31px;top:556px">Have you had a joint replacement?</span>
    <span class="a" style="left:204px;top:556px">Yes</span><span class="box" style="left:225px;top:556px"></span>
    <span class="a" style="left:241px;top:556px">No</span><span class="box" style="left:258px;top:556px"></span>

    <span class="a bold" style="left:31px;top:579px">Women:</span>
    <span class="a bold" style="left:31px;top:594px">Are you pregnant?</span>
    <span class="a" style="left:126px;top:594px">Yes</span><span class="box" style="left:150px;top:594px"></span>
    <span class="a" style="left:170px;top:594px">No</span><span class="box" style="left:190px;top:594px"></span>
    <span class="a" style="left:214px;top:594px">Possible</span><span class="box" style="left:254px;top:594px"></span>
    <span class="a" style="left:274px;top:594px">or</span>
    <span class="a bold" style="left:31px;top:610px">Breast Feeding?</span>
    <span class="a" style="left:126px;top:610px">Yes</span><span class="box" style="left:150px;top:610px"></span>
    <span class="a" style="left:170px;top:610px">No</span><span class="box" style="left:190px;top:610px"></span>

    <span class="turnover">Please Turnover</span>
    <div class="band band--bottom"><i></i><i></i><i></i><i></i></div>
  </section>

  <section class="page page--history" aria-label="Page two: medical history">
    <div class="band band--top"><i></i><i></i><i></i><i></i></div>

    <div class="brand" style="left:29px;top:40px;font-size:22px">Facet Dental</div>

    <p class="question">Do you have, or have you had, any of the following?</p>

    <div class="col col--left" style="top:0;height:600px">
      <div class="group" style="top:99px">
        <div class="group__title">Dental</div>
        <div class="row">Acid Reflux<span class="y">Yes</span><span class="box by"></span><span class="n">No</span><span class="box bn"></span></div>
        <div class="row">Bad Breath/Taste<span class="y">Yes</span><span class="box by"></span><span class="n">No</span><span class="box bn"></span></div>
        <div class="row">Bleeding/Swollen/Sore Gums<span class="y">Yes</span><span class="box by"></span><span class="n">No</span><span class="box bn"></span></div>
        <div class="row">Blisters/Ulcers in Mouth<span class="y">Yes</span><span class="box by"></span><span class="n">No</span><span class="box bn"></span></div>
        <div class="row">Broken tooth/filling<span class="y">Yes</span><span class="box by"></span><span class="n">No</span><span class="box bn"></span></div>
        <div class="row">Burning tongue<span class="y">Yes</span><span class="box by"></span><span class="n">No</span><span class="box bn"></span></div>
        <div class="row">Dry mouth<span class="y">Yes</span><span class="box by"></span><span class="n">No</span><span class="box bn"></span></div>
        <div class="row">Food collection between teeth<span class="y">Yes</span><span class="box by"></span><span class="n">No</span><span class="box bn"></span></div>
        <div class="row">Grinding/clenching teeth (day/night)<span class="y">Yes</span><span class="box by"></span><span class="n">No</span><span class="box bn"></span></div>
        <div class="row">Loose teeth<span class="y">Yes</span><span class="box by"></span><span class="n">No</span><span class="box bn"></span></div>
        <div class="row">Crooked teeth<span class="y">Yes</span><span class="box by"></span><span class="n">No</span><span class="box bn"></span></div>
        <div class="row">Discoloured teeth<span class="y">Yes</span><span class="box by"></span><span class="n">No</span><span class="box bn"></span></div>
        <div class="row">Sensitivity to Hot/Cold<span class="y">Yes</span><span class="box by"></span><span class="n">No</span><span class="box bn"></span></div>
        <div class="row">Tooth pain when chewing<span class="y">Yes</span><span class="box by"></span><span class="n">No</span><span class="box bn"></span></div>
        <div class="row">Jaw pain/Fracture<span class="y">Yes</span><span class="box by"></span><span class="n">No</span><span class="box bn"></span></div>
        <div class="row">Orthodontic treatment/history<span class="y">Yes</span><span class="box by"></span><span class="n">No</span><span class="box bn"></span></div>
        <div class="row">Oral Cancer<span class="y">Yes</span><span class="box by"></span><span class="n">No</span><span class="box bn"></span></div>
      </div>

      <div class="group" style="top:297px">
        <div class="group__title">Diet/Lifestyle</div>
        <div class="row row--tall">Drink more than one<br>glass alcohol per day<span class="y">Yes</span><span class="box by"></span><span class="n">No</span><span class="box bn"></span></div>
        <div class="row">Smoking<span class="y">Yes</span><span class="box by"></span><span class="n">No</span><span class="box bn"></span></div>
        <div class="row">Carbonated drinks<span class="y">Yes</span><span class="box by"></span><span class="n">No</span><span class="box bn"></span></div>
        <div class="row">Sugary foods<span class="y">Yes</span><span class="box by"></span><span class="n">No</span><span class="box bn"></span></div>
      </div>

      <div class="group" style="top:369px">
        <div class="group__title">Blood</div>
        <div class="row">Anaemia<span class="y">Yes</span><span class="box by"></span><span class="n">No</span><span class="box bn"></span></div>
        <div class="row">Blood clots<span class="y">Yes</span><span class="box by"></span><span class="n">No</span><span class="box bn"></span></div>
        <div class="row">Leukemia<span class="y">Yes</span><span class="box by"></span><span class="n">No</span><span class="box bn"></span></div>
        <div class="row">Low platelets<span class="y">Yes</span><span class="box by"></span><span class="n">No</span><span class="box bn"></span></div>
        <div class="row">Lymphoma<span class="y">Yes</span><span class="box by"></span><span class="n">No</span><span class="box bn"></span></div>
        <div class="row">Haemophelia<span class="y">Yes</span><span class="box by"></span><span class="n">No</span><span class="box bn"></span></div>
      </div>

      <div class="group" style="top:452px">
        <div class="group__title">Chest</div>
        <div class="row">Bronchitis<span class="y">Yes</span><span class="box by"></span><span class="n">No</span><span class="box bn"></span></div>
        <div class="row">Cystic Fibrosis<span class="y">Yes</span><span class="box by"></span><span class="n">No</span><span class="box bn"></span></div>
        <div class="row">Emphysema<span class="y">Yes</span><span class="box by"></span><span class="n">No</span><span class="box bn"></span></div>
        <div class="row">Pneumonia<span class="y">Yes</span><span class="box by"></span><span class="n">No</span><span class="box bn"></span></div>
      </div>

      <div class="group" style="top:515px">
        <div class="group__title">Infectious Disease</div>
        <div class="row">Creutzfeldt-Jakob Disease<span class="y">Yes</span><span class="box by"></span><span class="n">No</span><span class="box bn"></span></div>
        <div class="row">Hepatitis A,B,C,D<span class="y">Yes</span><span class="box by"></span><span class="n">No</span><span class="box bn"></span></div>
        <div class="row">HIV/AIDS<span class="y">Yes</span><span class="box by"></span><span class="n">No</span><span class="box bn"></span></div>
        <div class="row">Influenza<span class="y">Yes</span><span class="box by"></span><span class="n">No</span><span class="box bn"></span></div>
        <div class="row">Shingles<span class="y">Yes</span><span class="box by"></span><span class="n">No</span><span class="box bn"></span></div>
        <div class="row">Tuberculosis<span class="y">Yes</span><span class="box by"></span><span class="n">No</span><span class="box bn"></span></div>
      </div>
    </div>

    <div class="col col--right" style="top:0;height:600px">
      <div class="group" style="top:101px">
        <div class="group__title">Heart</div>
        <div class="row">Angina<span class="y">Yes</span><span class="box by"></span><span class="n">No</span><span class="box bn"></span></div>
        <div class="row">Atrial Fibrillation<span class="y">Yes</span><span class="box by"></span><span class="n">No</span><span class="box bn"></span></div>
        <div class="row">Blood Pressure (High/Low)<span class="y">Yes</span><span class="box by"></span><span class="n">No</span><span class="box bn"></span></div>
        <div class="row">Congenital Heart Disease<span class="y">Yes</span><span class="box by"></span><span class="n">No</span><span class="box bn"></span></div>
        <div class="row">Heart attack<span class="y">Yes</span><span class="box by"></span><span class="n">No</span><span class="box bn"></span></div>
        <div class="row">Heart murmur<span class="y">Yes</span><span class="box by"></span><span class="n">No</span><span class="box bn"></span></div>
        <div class="row">Heart surgery<span class="y">Yes</span><span class="box by"></span><span class="n">No</span><span class="box bn"></span></div>
        <div class="row">Heart valve replacement<span class="y">Yes</span><span class="box by"></span><span class="n">No</span><span class="box bn"></span></div>
        <div class="row">Infective endocarditis<span class="y">Yes</span><span class="box by"></span><span class="n">No</span><span class="box bn"></span></div>
        <div class="row">Rheumatic Heart Disease<span class="y">Yes</span><span class="box by"></span><span class="n">No</span><span class="box bn"></span></div>
        <div class="row">Pacemaker<span class="y">Yes</span><span class="box by"></span><span class="n">No</span><span class="box bn"></span></div>
        <div class="row">Stent<span class="y">Yes</span><span class="box by"></span><span class="n">No</span><span class="box bn"></span></div>
      </div>

      <div class="group" style="top:249px">
        <div class="group__title">Other</div>
        <div class="row">Anxiety/PTSD<span class="y">Yes</span><span class="box by"></span><span class="n">No</span><span class="box bn"></span></div>
        <div class="row">Arthritis<span class="y">Yes</span><span class="box by"></span><span class="n">No</span><span class="box bn"></span></div>
        <div class="row">Alzheimer's<span class="y">Yes</span><span class="box by"></span><span class="n">No</span><span class="box bn"></span></div>
        <div class="row">Asthma<span class="y">Yes</span><span class="box by"></span><span class="n">No</span><span class="box bn"></span></div>
        <div class="row">Anaphylaxis<span class="y">Yes</span><span class="box by"></span><span class="n">No</span><span class="box bn"></span></div>
        <div class="row">Auto-immune disease<span class="y">Yes</span><span class="box by"></span><span class="n">No</span><span class="box bn"></span></div>
        <div class="row">Coeliac<span class="y">Yes</span><span class="box by"></span><span class="n">No</span><span class="box bn"></span></div>
        <div class="row">Depression<span class="y">Yes</span><span class="box by"></span><span class="n">No</span><span class="box bn"></span></div>
        <div class="row">Diabetes<span class="y">Yes</span><span class="box by"></span><span class="n">No</span><span class="box bn"></span></div>
        <div class="row">Epilepsy<span class="y">Yes</span><span class="box by"></span><span class="n">No</span><span class="box bn"></span></div>
        <div class="row">Kidney Disease<span class="y">Yes</span><span class="box by"></span><span class="n">No</span><span class="box bn"></span></div>
        <div class="row">Liver Disease<span class="y">Yes</span><span class="box by"></span><span class="n">No</span><span class="box bn"></span></div>
        <div class="row">Osteoporosis<span class="y">Yes</span><span class="box by"></span><span class="n">No</span><span class="box bn"></span></div>
        <div class="row">Parkinson's<span class="y">Yes</span><span class="box by"></span><span class="n">No</span><span class="box bn"></span></div>
        <div class="row">Radiation to Head/Neck<span class="y">Yes</span><span class="box by"></span><span class="n">No</span><span class="box bn"></span></div>
        <div class="row">Schizophrenia<span class="y">Yes</span><span class="box by"></span><span class="n">No</span><span class="box bn"></span></div>
        <div class="row">Snoring<span class="y">Yes</span><span class="box by"></span><span class="n">No</span><span class="box bn"></span></div>
        <div class="row">Sleep apnea<span class="y">Yes</span><span class="box by"></span><span class="n">No</span><span class="box bn"></span></div>
        <div class="row">Stroke<span class="y">Yes</span><span class="box by"></span><span class="n">No</span><span class="box bn"></span></div>
      </div>

      <div class="field" style="left:0;right:22px;top:481px;font-size:8.3px"><span>Other:&nbsp;</span><span class="line"></span></div>
    </div>

    <div class="field" style="left:20px;width:251px;top:607px;font-size:8.3px"><span>Signature:</span><span class="line"></span></div>
    <div class="field" style="left:315px;width:143px;top:607px;font-size:8.3px"><span>Date:</span><span class="line"></span></div>

    <p class="thanks">Thank you for the time to complete your medical history form.<br>Oral health is linked to overall health and this comprehensive questionnaire will help us<br>to provide you with optimal and safe care.</p>

    <div class="band band--bottom"><i></i><i></i><i></i><i></i></div>
  </section>

</main>
</body>
</html>
```